Build a Website for Pharmacy Stores company

We are looking to build a modern website for our Pharmacy Stores.

The goal of the website is to inform customers about us, our locations, blog posts, promotion section, etc..
We are thinking of having the homepage as a digest of all the pages. Please see attached suggested pages and their descriptions.

Design: creative, clean and modern; similar to material design is nice! Should have some professional feel to it. No cheap design, no ready made templates!
Color scheme should match the logo (color green with some grey) make it work! Don't style the pages around the old logo as it is about to be replaced.

Development: Dynamic content, wordpress preferred, must be responsive, mobile friendly.

Please do not submit generic templates as your submission, you will be disqualified.

```html
<!DOCTYPE html>
<html lang="en">
<head>
<meta charset="utf-8">
<title>Medora Pharmacies</title>
<link href="https://fonts.googleapis.com/css2?family=Roboto+Condensed:wght@300;400;700&family=Roboto:wght@400;500;700&display=swap" rel="stylesheet">
<style>
:root{
  --green:#7cbf2f;--green-dark:#5f9a1e;--blue:#0e4f94;--blue-dark:#0a3f7a;
  --ink:#2b2b2b;--text:#555;--grey:#8a8a8a;--dark:#333;--panel:#2e3642;
  --news-bg:#3a4454;--white:#fff;--line:#e4e4e4;
}
*{box-sizing:border-box;margin:0;padding:0}
html,body{width:1200px;height:4937px;overflow:hidden}
body{font-family:'Roboto',sans-serif;color:var(--text);background:var(--white);position:relative}
.abs{position:absolute}
.heading{font-family:'Roboto Condensed',sans-serif;font-weight:700;color:var(--green);text-transform:uppercase}

/* header */
.topbar{top:0;left:0;width:1200px;height:88px}
.brand{left:78px;top:18px;display:flex;align-items:center;gap:10px;font-family:'Roboto Condensed',sans-serif;font-weight:700;font-size:18px;color:var(--green-dark)}
.brand .mark{width:26px;height:26px;border-radius:50%;background:var(--green-dark)}
.social{top:30px;left:850px;display:flex;gap:8px}
.social span{width:28px;height:28px;background:var(--blue);display:block}
.lang{top:28px;left:988px;width:132px;height:34px;border:1px solid #ccc;display:flex;align-items:center;gap:10px;padding:0 10px;font-size:11px;font-weight:700;color:var(--ink)}
.lang i{width:24px;height:14px;background:#c8ced8;display:block}
.navbar{top:88px;left:0;width:1200px;height:54px;background:var(--green)}
.navbar a{position:absolute;top:0;height:54px;line-height:54px;color:#fff;font-size:12px;font-weight:500;text-decoration:none;transform:translateX(-50%);white-space:nowrap}
.navbar a.active{background:var(--green-dark);width:104px;text-align:center}

/* hero */
.hero{top:142px;left:0;width:1200px;height:525px;background:linear-gradient(100deg,#b9c7cf 0%,#dfe6ea 45%,#c9d6de 100%)}
.hero-badge{left:727px;top:240px;width:364px;height:364px;border-radius:50%;background:var(--green);text-align:center;color:#fff}
.hero-badge h1{font-family:'Roboto Condensed',sans-serif;font-weight:700;line-height:1;margin-top:128px}
.hero-badge h1 .l1{display:block;font-size:40px}
.hero-badge h1 .l2{display:block;font-size:62px}
.hero-badge p{font-size:11px;width:230px;margin:10px auto 0;line-height:1.4}
.contact{top:667px;left:0;width:1200px;height:138px;background:var(--blue)}
.contact .side{left:0;top:0;width:398px;height:138px;background:var(--blue-dark)}
.contact div.item{top:50px;color:#fff;font-size:18px;font-weight:700;line-height:1.3}

/* about */
.about-title{top:860px;width:1200px;text-align:center;font-size:40px}
.about-quote{top:906px;width:1200px;text-align:center;font-family:'Roboto Condensed',sans-serif;font-style:italic;font-weight:300;font-size:25px;color:var(--ink)}
.about-text{top:964px;left:110px;width:980px;text-align:center;font-size:11px;line-height:1.6;color:var(--ink)}
.values-title{top:1052px;left:78px;font-family:'Roboto Condensed',sans-serif;font-weight:700;font-size:25px;color:var(--grey);display:flex;align-items:center;gap:12px}
.values-title::after{content:"";width:74px;height:2px;background:var(--grey)}
.value{width:230px}
.value h3{display:flex;align-items:center;gap:10px;font-size:16px;font-weight:400;color:var(--ink);margin-bottom:14px}
.value h3 svg{flex:none}
.value p{font-size:11px;line-height:1.6}
.about-photo{left:617px;top:1052px;width:504px;height:382px;background:linear-gradient(135deg,#e9eef0,#cfd9dd)}

/* stores */
.stores{top:1495px;left:0;width:1200px;height:560px;background:#eef0ee}
.stores-card{left:128px;top:1553px;width:955px;height:425px;background:#fff;box-shadow:0 4px 18px rgba(0,0,0,.25);overflow:hidden}
.stores-card header{height:61px;background:var(--green);text-align:center;line-height:61px;font-size:36px;color:#fff}
.store-row{position:absolute;left:16px;width:900px;height:96px;border-bottom:1px solid var(--line);box-shadow:0 2px 4px rgba(0,0,0,.08)}
.store-row .ico{position:absolute;left:14px;top:22px;width:50px;height:50px;background:#eceff1;border-radius:3px}
.store-row .ico i{position:absolute;left:10px;top:12px;width:30px;height:24px;border:3px solid #d33;border-top-width:8px}
.store-row h4{position:absolute;left:92px;top:16px;font-size:14px;font-weight:500;color:var(--ink)}
.store-row .meta{position:absolute;top:52px;display:flex;align-items:center;gap:8px;font-size:11px;color:var(--ink)}
.store-row .btn{position:absolute;left:732px;top:38px;width:158px;height:38px;background:var(--blue);color:#fff;font-size:11px;text-align:center;line-height:38px}
.scrollbar{right:14px;top:80px;width:4px;height:335px;background:#eee}
.scrollbar i{display:block;width:4px;height:120px;background:#bbb}

/* promotion */
.promo{top:2055px;left:0;width:1200px;height:623px;background:linear-gradient(90deg,#3d4248,#2c3035)}
.promo-photo{left:0;top:2098px;width:500px;height:555px;border-radius:0 50% 50% 45%;background:linear-gradient(135deg,#f4c63c,#eab08a 40%,#d7dde2 75%)}
.promo-title{left:609px;top:2163px;font-size:38px}
.promo-text{left:609px;width:518px;font-size:10.5px;line-height:1.65;color:#e6e6e6}
.btn-green{left:609px;top:2477px;width:152px;height:46px;background:var(--green);color:#fff;font-size:13px;line-height:46px;padding-left:32px}

/* products */
.products-panel{top:2678px;left:543px;width:657px;height:696px;background:#333}
.products-title{left:102px;top:2738px;font-size:38px;display:flex;align-items:center;gap:14px}
.products-title::after{content:"";width:74px;height:2px;background:var(--green)}
.products-photo{left:100px;top:2812px;width:489px;height:491px;background:linear-gradient(135deg,#f0d9b8,#e7e2da 45%,#cf4a3f 100%);box-shadow:0 6px 16px rgba(0,0,0,.35)}
.brand-tile{width:251px;height:192px;background:#fff;display:flex;align-items:center;justify-content:center;gap:10px;font-size:18px;font-weight:700;color:var(--green-dark)}
.brand-tile i{width:22px;height:22px;border-radius:50%;background:var(--green-dark);display:block}
.arrow-next{left:1140px;top:3045px}

/* blog */
.blog-title{top:3420px;width:1200px;text-align:center;font-size:38px}
.post{width:339px}
.post .thumb{height:230px;background:linear-gradient(135deg,#d9e3e8,#f1f4f5 50%,#c7d3da);position:relative}
.post .date{position:absolute;left:14px;top:0;width:58px;height:70px;background:var(--green);color:#fff;font-size:12px;font-weight:700;text-align:center;padding-top:14px;line-height:1.2}
.post h3{font-size:20px;font-weight:500;color:var(--ink);line-height:1.2;margin:36px 0 12px}
.post p{font-size:11.5px;line-height:1.65}

/* news */
.news{top:3962px;left:0;width:1200px;height:735px;background:linear-gradient(135deg,#2f3a4e,#4a5566 60%,#3b4a3c)}
.news-title{top:4004px;width:1200px;text-align:center;font-family:'Roboto Condensed',sans-serif;font-weight:700;font-size:36px;color:#fff}
.news-title::after{content:"";display:block;width:40px;height:2px;background:#fff;margin:10px auto 0}
.news-card{width:511px;height:240px;background:rgba(40,46,56,.8);box-shadow:0 4px 14px rgba(0,0,0,.4);color:#eee}
.news-card .day{position:absolute;left:20px;top:26px;width:80px;height:110px;background:var(--green);color:#fff;text-align:center;font-family:'Roboto Condensed',sans-serif;font-weight:700}
.news-card .day b{display:block;font-size:60px;line-height:70px}
.news-card .day span{font-size:20px}
.news-card h4{position:absolute;left:124px;top:30px;font-size:15px;font-weight:700;color:#fff}
.news-card p{position:absolute;left:124px;width:360px;font-size:11px;line-height:1.6}

/* newsletter & footer */
.newsletter{top:4697px;left:0;width:1200px;height:115px;background:linear-gradient(90deg,#4b2fa8,#3f3fc4 50%,#2f7ae0)}
.newsletter h5{position:absolute;left:78px;top:40px;font-family:'Roboto Condensed',sans-serif;font-weight:400;font-size:24px;color:#fff}
.newsletter .field{position:absolute;left:537px;top:36px;width:442px;height:44px;border:1px solid rgba(255,255,255,.7);color:#ddd;font-size:11px;line-height:42px;padding-left:18px}
.newsletter .submit{position:absolute;left:979px;top:36px;width:142px;height:44px;background:#111;color:#fff;font-size:11px;text-align:center;line-height:44px}
.footer{top:4812px;left:0;width:1200px;height:125px;background:#333;color:#fff}
.footer a{position:absolute;top:24px;font-size:12px;color:#fff;text-decoration:none;transform:translateX(-50%);white-space:nowrap}
.footer small{position:absolute;left:78px;top:80px;font-size:11px;color:#ddd}
.footer .chat{position:absolute;left:900px;top:70px;font-size:17px;font-weight:700;display:flex;align-items:center;gap:12px}
.footer .chat i{width:40px;height:40px;border-radius:50%;background:#eee;display:block}
</style>
</head>
<body>

<header class="abs topbar">
  <div class="abs brand"><span class="mark"></span>Medora Pharmacies</div>
  <div class="abs social" aria-label="Social links"><span></span><span></span><span></span></div>
  <div class="abs lang"><i></i>ENGLISH
    <svg width="10" height="6" viewBox="0 0 10 6"><path d="M0 0h10L5 6z" fill="#333"/></svg></div>
</header>

<nav class="abs navbar">
  <a class="active" style="left:132px">Home</a>
  <a style="left:236px">About Us</a>
  <a style="left:353px">Find A Store</a>
  <a style="left:475px">Promotion</a>
  <a style="left:621px">Inspiration &amp; Advice</a>
  <a style="left:780px">News &amp; Events</a>
  <a style="left:934px">Products &amp; Brands</a>
  <a style="left:1062px">Others</a>
</nav>

<section class="abs hero" role="img" aria-label="Pharmacist helping a customer choose a product in a pharmacy aisle"></section>
<div class="abs hero-badge">
  <h1><span class="l1">ALWAYS HERE</span><span class="l2">TO CARE</span></h1>
  <p>Our vision is to be a nationally recognized leader in providing the highest quality and most trusted</p>
</div>

<section class="abs contact">
  <div class="abs side"></div>
  <div class="abs item" style="left:126px">Call Us:<br>(123) 456 7890</div>
  <div class="abs item" style="left:483px">Email:<br>info@companyname.com</div>
  <div class="abs item" style="left:853px">Address:<br>62, loremipsum dolor sit</div>
</section>

<h2 class="abs heading about-title">About Us</h2>
<p class="abs about-quote">“Always Here To Care”</p>
<p class="abs about-text">“MEDORA PHARMACIES GROUP” is a Fast-Growing retail pharmacy company established in Kuwait 2007. Our mission is to create emotional bond with our customers by providing the at most in expert advice, friendly service and high quality products. Our vision is to be a nationally recognized leader in providing the highest quality and most trusted</p>

<h3 class="abs values-title">Values</h3>
<div class="abs value" style="left:78px;top:1104px">
  <h3><svg width="34" height="34" viewBox="0 0 34 34"><circle cx="17" cy="17" r="14" fill="none" stroke="#7cbf2f" stroke-width="2"/><path d="M10 17l5 5 9-10" fill="none" stroke="#7cbf2f" stroke-width="2.5"/></svg>Integrity</h3>
  <p>We are committed to the highest standards of professionalism, honesty and fairness in our relationships.</p>
</div>
<div class="abs value" style="left:305px;top:1104px">
  <h3><svg width="34" height="34" viewBox="0 0 34 34"><rect x="5" y="4" width="24" height="26" rx="2" fill="none" stroke="#7cbf2f" stroke-width="2"/><path d="M11 12h12M11 18h12M11 24h8" stroke="#7cbf2f" stroke-width="2"/></svg>Compassion</h3>
  <p>Bringing Humanity to our Work: a deep feeling for and understanding of others without regard to race, age creed, or social standing.</p>
</div>
<div class="abs value" style="left:78px;top:1232px">
  <h3><svg width="34" height="34" viewBox="0 0 34 34"><circle cx="17" cy="11" r="6" fill="none" stroke="#7cbf2f" stroke-width="2"/><path d="M6 31c0-7 5-11 11-11s11 4 11 11" fill="none" stroke="#7cbf2f" stroke-width="2"/></svg>Respect</h3>
  <p>We treat everyone with honesty, decency and fairness.</p>
</div>
<div class="abs value" style="left:305px;top:1232px">
  <h3><svg width="34" height="34" viewBox="0 0 34 34"><path d="M17 30S4 22 4 13a7 7 0 0 1 13-3 7 7 0 0 1 13 3c0 9-13 17-13 17z" fill="none" stroke="#7cbf2f" stroke-width="2"/></svg>Social Responsibility(CSR)</h3>
  <p>Has a deeply rooted tradition of acting in a responsible and ethical manner, and being actively and positively present in the communities where it is established.</p>
</div>
<div class="abs value" style="left:78px;top:1332px;width:390px">
  <h3><svg width="34" height="34" viewBox="0 0 34 34"><circle cx="17" cy="17" r="13" fill="none" stroke="#7cbf2f" stroke-width="2"/><path d="M17 10v14M10 17h14" stroke="#7cbf2f" stroke-width="2"/></svg>Professionalism</h3>
  <p>We are committed to being the best in what we do, and to achieving the best possible outcome for our patients.</p>
</div>
<div class="abs about-photo" role="img" aria-label="Smiling pharmacist in a white coat holding a red heart"></div>

<section class="abs stores" role="img" aria-label="Faint street map of store locations"></section>
<div class="abs stores-card">
  <header class="heading">Find A Stores</header>
  <div class="store-row" style="top:70px">
    <div class="ico"><i></i></div><h4>Lorem ipsum dolor sit amet</h4>
    <div class="meta" style="left:92px"><svg width="18" height="18" viewBox="0 0 18 18"><circle cx="9" cy="9" r="7" fill="none" stroke="#e8453c" stroke-width="2"/><path d="M9 5v4l3 2" stroke="#e8453c" stroke-width="2" fill="none"/></svg>Opening hours: 12 Hours</div>
    <div class="meta" style="left:290px"><svg width="16" height="20" viewBox="0 0 16 20"><path d="M8 0a7 7 0 0 1 7 7c0 5-7 13-7 13S1 12 1 7a7 7 0 0 1 7-7z" fill="#e8453c"/><circle cx="8" cy="7" r="2.5" fill="#fff"/></svg>Address: 62 Lorem ipsum Dolor Sit</div>
    <div class="meta" style="left:530px"><svg width="20" height="20" viewBox="0 0 20 20"><path d="M4 1l4 4-2 3c1 3 3 5 6 6l3-2 4 4-3 3C8 19 1 12 1 4z" fill="#5f9a1e"/></svg>Call us: (123) 456 7890</div>
    <div class="btn">Get Direction</div>
  </div>
  <div class="store-row" style="top:181px">
    <div class="ico"><i></i></div><h4>Lorem ipsum dolor sit amet</h4>
    <div class="meta" style="left:92px"><svg width="18" height="18" viewBox="0 0 18 18"><circle cx="9" cy="9" r="7" fill="none" stroke="#e8453c" stroke-width="2"/><path d="M9 5v4l3 2" stroke="#e8453c" stroke-width="2" fill="none"/></svg>Opening hours: 12 Hours</div>
    <div class="meta" style="left:290px"><svg width="16" height="20" viewBox="0 0 16 20"><path d="M8 0a7 7 0 0 1 7 7c0 5-7 13-7 13S1 12 1 7a7 7 0 0 1 7-7z" fill="#e8453c"/><circle cx="8" cy="7" r="2.5" fill="#fff"/></svg>Address: 62 Lorem ipsum Dolor Sit</div>
    <div class="meta" style="left:530px"><svg width="20" height="20" viewBox="0 0 20 20"><path d="M4 1l4 4-2 3c1 3 3 5 6 6l3-2 4 4-3 3C8 19 1 12 1 4z" fill="#5f9a1e"/></svg>Call us: (123) 456 7890</div>
    <div class="btn">Get Direction</div>
  </div>
  <div class="store-row" style="top:292px">
    <div class="ico"><i></i></div><h4>Lorem ipsum dolor sit amet</h4>
    <div class="meta" style="left:92px"><svg width="18" height="18" viewBox="0 0 18 18"><circle cx="9" cy="9" r="7" fill="none" stroke="#e8453c" stroke-width="2"/><path d="M9 5v4l3 2" stroke="#e8453c" stroke-width="2" fill="none"/></svg>Opening hours: 12 Hours</div>
    <div class="meta" style="left:290px"><svg width="16" height="20" viewBox="0 0 16 20"><path d="M8 0a7 7 0 0 1 7 7c0 5-7 13-7 13S1 12 1 7a7 7 0 0 1 7-7z" fill="#e8453c"/><circle cx="8" cy="7" r="2.5" fill="#fff"/></svg>Address: 62 Lorem ipsum Dolor Sit</div>
    <div class="meta" style="left:530px"><svg width="20" height="20" viewBox="0 0 20 20"><path d="M4 1l4 4-2 3c1 3 3 5 6 6l3-2 4 4-3 3C8 19 1 12 1 4z" fill="#5f9a1e"/></svg>Call us: (123) 456 7890</div>
    <div class="btn">Get Direction</div>
  </div>
  <div class="store-row" style="top:403px;opacity:.4">
    <div class="ico"><i></i></div><h4>Lorem ipsum dolor sit amet</h4><div class="btn"></div>
  </div>
  <div class="abs scrollbar"><i></i></div>
</div>

<section class="abs promo" role="img" aria-label="Pharmacy interior in dark tones"></section>
<div class="abs promo-photo" role="img" aria-label="Mother with her child receiving a product from a pharmacist"></div>
<h2 class="abs heading promo-title">Promotion</h2>
<p class="abs promo-text" style="top:2218px">Lorem ipsum dolor sit amet, consectetur adipiscing elit. Aenean sodales lectus vitae orci pulvinar sodales. Fusce convallis congue nunc, in varius neque iaculis nec. Curabitur accumsan dui placerat condimentum venenatis. Nullam porttitor scelerisque dolor, sed ultrices velit venenatis nec. Ut pulvinar, orci in hendrerit bibendum, mauris tortor faucibus magna, ac lobortis nunc massa at neque.</p>
<p class="abs promo-text" style="top:2302px">Lorem ipsum dolor sit amet, consectetur adipiscing elit. Aenean sodales lectus vitae orci pulvinar sodales. Fusce convallis congue nunc, in varius neque iaculis nec. Curabitur accumsan dui placerat condimentum venenatis. Nullam porttitor scelerisque dolor, sed ultrices velit venenatis nec. Ut pulvinar, orci in hendrerit bibendum, mauris tortor faucibus magna, ac lobortis nunc massa at neque.</p>
<p class="abs promo-text" style="top:2388px">Lorem ipsum dolor sit amet, consectetur adipiscing elit. Aenean sodales lectus vitae orci pulvinar sodales. Fusce convallis congue nunc, in varius neque iaculis nec. Curabitur accumsan dui placerat condimentum venenatis. Nullam porttitor scelerisque dolor, sed ultrices velit venenatis nec. Ut pulvinar, orci in hendrerit bibendum, mauris tortor faucibus magna, ac lobortis nunc massa at neque.</p>
<div class="abs btn-green">Read More &nbsp;›</div>

<section class="abs products-panel"></section>
<h2 class="abs heading products-title">Products</h2>
<div class="abs products-photo" role="img" aria-label="Woman reading the label on a box of pills"></div>
<div class="abs brand-tile" style="left:602px;top:2858px"><i></i>Linden Pharmacy</div>
<div class="abs brand-tile" style="left:868px;top:2858px"><i></i>Brightway Pharmacy</div>
<div class="abs brand-tile" style="left:602px;top:3067px"><i></i>Kindwell Pharmacy</div>
<div class="abs brand-tile" style="left:868px;top:3067px"><i></i>Orrin Pharmacy</div>
<svg class="abs arrow-next" width="16" height="28" viewBox="0 0 16 28"><path d="M2 2l12 12L2 26" fill="none" stroke="#bbb" stroke-width="2"/></svg>

<h2 class="abs heading blog-title">Blog</h2>
<article class="abs post" style="left:79px;top:3493px">
  <div class="thumb" role="img" aria-label="Pharmacist handing medicine to an older customer"><div class="date">25 OCT<br>2018</div></div>
  <h3>Lorem ipsum dolor sit amet, consectetur adipiscing eli</h3>
  <p>Lorem ipsum dolor sit amet, consectetur adipiscing elit. Aenean sodales lectus vitae orci pulvinar sodales. Fusce convallis congue nunc, in varius neque iaculis nec. Curabitur accumsan dui placerat condimentum venenatis.</p>
</article>
<article class="abs post" style="left:431px;top:3493px">
  <div class="thumb" role="img" aria-label="Team of pharmacists standing in a pharmacy"><div class="date">25 OCT<br>2018</div></div>
  <h3>Lorem ipsum dolor sit amet, consectetur adipiscing eli</h3>
  <p>Lorem ipsum dolor sit amet, consectetur adipiscing elit. Aenean sodales lectus vitae orci pulvinar sodales. Fusce convallis congue nunc, in varius neque iaculis nec. Curabitur accumsan dui placerat condimentum venenatis.</p>
</article>
<article class="abs post" style="left:782px;top:3493px">
  <div class="thumb" role="img" aria-label="Pharmacist advising a mother holding a baby"><div class="date">25 OCT<br>2018</div></div>
  <h3>Lorem ipsum dolor sit amet, consectetur adipiscing eli</h3>
  <p>Lorem ipsum dolor sit amet, consectetur adipiscing elit. Aenean sodales lectus vitae orci pulvinar sodales. Fusce convallis congue nunc, in varius neque iaculis nec. Curabitur accumsan dui placerat condimentum venenatis.</p>
</article>

<section class="abs news" role="img" aria-label="Blurred pharmacy shelves background"></section>
<h2 class="abs news-title">Latest News &amp; Events</h2>
<div class="abs news-card" style="left:79px;top:4083px">
  <div class="day"><b>06</b><span>2018</span></div><h4>Lorem ipsum dolor sit amet</h4>
  <p style="top:62px">Lorem ipsum dolor sit amet, consectetur adipiscing elit. Aenean sodales lectus vitae orci pulvinar sodales. Fusce convallis congue nunc, in varius neque iaculis nec.</p>
  <p style="top:128px">Lorem ipsum dolor sit amet, consectetur adipiscing elit. Aenean sodales lectus</p>
</div>
<div class="abs news-card" style="left:610px;top:4083px">
  <div class="day"><b>09</b><span>2018</span></div><h4>Lorem ipsum dolor sit amet</h4>
  <p style="top:62px">Lorem ipsum dolor sit amet, consectetur adipiscing elit. Aenean sodales lectus vitae orci pulvinar sodales. Fusce convallis congue nunc, in varius neque iaculis nec.</p>
  <p style="top:128px">Lorem ipsum dolor sit amet, consectetur adipiscing elit. Aenean sodales lectus</p>
</div>
<div class="abs news-card" style="left:79px;top:4376px">
  <div class="day"><b>06</b><span>2018</span></div><h4>Lorem ipsum dolor sit amet</h4>
  <p style="top:62px">Lorem ipsum dolor sit amet, consectetur adipiscing elit. Aenean sodales lectus vitae orci pulvinar sodales. Fusce convallis congue nunc, in varius neque iaculis nec.</p>
  <p style="top:128px">Lorem ipsum dolor sit amet, consectetur adipiscing elit. Aenean sodales lectus</p>
</div>
<div class="abs news-card" style="left:610px;top:4376px">
  <div class="day"><b>09</b><span>2018</span></div><h4>Lorem ipsum dolor sit amet</h4>
  <p style="top:62px">Lorem ipsum dolor sit amet, consectetur adipiscing elit. Aenean sodales lectus vitae orci pulvinar sodales. Fusce convallis congue nunc, in varius neque iaculis nec.</p>
  <p style="top:128px">Lorem ipsum dolor sit amet, consectetur adipiscing elit. Aenean sodales lectus</p>
</div>

<section class="abs newsletter">
  <h5>Sign Up to Get Our Promotion and Newsletter</h5>
  <div class="field">Enter Email Address</div>
  <div class="submit">Submit</div>
</section>

<footer class="abs footer">
  <a style="left:143px">Home</a>
  <a style="left:246px">About Us</a>
  <a style="left:362px">Find A Store</a>
  <a style="left:482px">Promotion</a>
  <a style="left:622px">Inspiration &amp; Advice</a>
  <a style="left:778px">News &amp; Events</a>
  <a style="left:927px">Products &amp; Brands</a>
  <a style="left:1053px">Others</a>
  <small>© Copyright 2018 Medora Pharmacies. All Rights Reserved.</small>
  <div class="chat">Customer WebChat <i></i></div>
</footer>

</body>
</html>
```